Need a webinar banner promo to place on social media

We are organise a series of webinars in coming months.

We need a webinar banner design to be posted on Facebook and linkedin. The banner is for our webinar titled: Steps to Unveil your venture with poise and polish.

our website is www.bravolinhub.com.au

there is a link on the website to the webinar registration for your reference.

```html
<!DOCTYPE html>
<html lang="en">
<head>
<meta charset="utf-8">
<title>Webinar – Steps to Unveil your venture with poise and polish</title>
<link rel="stylesheet" href="https://fonts.googleapis.com/css2?family=Montserrat:ital,wght@0,300;0,400;0,600;0,700;1,300&display=swap">
<style>
  :root {
    --navy: #0e1f3e;
    --navy-deep: #0a1730;
    --gold: #d2ad45;
    --gold-light: #e8c65a;
    --gold-dark: #a9842a;
    --white: #ffffff;
    --photo-a: #2a4a86;
    --photo-b: #8a4a5a;
    --photo-c: #c7b9a8;
  }
  html, body {
    margin: 0;
    padding: 0;
    width: 1200px;
    height: 1200px;
    overflow: hidden;
    background: var(--navy);
  }
  .banner {
    position: relative;
    width: 1200px;
    height: 1200px;
    overflow: hidden;
    background: var(--navy);
    font-family: "Montserrat", sans-serif;
    color: var(--white);
  }
  .banner__art {
    position: absolute;
    inset: 0;
    width: 1200px;
    height: 1200px;
  }
  .brand {
    position: absolute;
    left: 880px;
    top: 690px;
    width: 280px;
    display: flex;
    align-items: center;
    gap: 12px;
    font-weight: 700;
    font-size: 40px;
    line-height: 1;
    color: var(--gold);
  }
  .brand__mark {
    width: 22px;
    height: 22px;
    background: var(--gold);
    flex: none;
  }
  .eyebrow {
    position: absolute;
    left: 62px;
    top: 708px;
    margin: 0;
    font-weight: 300;
    font-size: 40px;
    line-height: 1;
  }
  .headline {
    position: absolute;
    left: 58px;
    top: 770px;
    margin: 0;
    font-weight: 700;
    font-size: 56px;
    line-height: 62px;
    letter-spacing: -0.5px;
  }
  .intro {
    position: absolute;
    left: 62px;
    top: 908px;
    width: 1060px;
    margin: 0;
    font-weight: 400;
    font-size: 20px;
    line-height: 30px;
  }
  .schedule {
    position: absolute;
    left: 62px;
    top: 1055px;
  }
  .schedule__label {
    margin: 0;
    font-weight: 700;
    font-size: 36px;
    line-height: 1.1;
  }
  .schedule__time {
    margin: 6px 0 0;
    font-weight: 300;
    font-style: italic;
    font-size: 36px;
    line-height: 1.1;
  }
  .site {
    position: absolute;
    left: 770px;
    top: 1118px;
    margin: 0;
    font-weight: 700;
    font-size: 22px;
  }
</style>
</head>
<body>
<main class="banner">
  <svg class="banner__art" viewBox="0 0 1200 1200" aria-hidden="false">
    <defs>
      <linearGradient id="photoTone" x1="0" y1="0" x2="1" y2="1">
        <stop offset="0" stop-color="var(--photo-a)"/>
        <stop offset="0.55" stop-color="var(--photo-b)"/>
        <stop offset="1" stop-color="var(--photo-c)"/>
      </linearGradient>
      <linearGradient id="goldTone" x1="0" y1="0" x2="1" y2="0">
        <stop offset="0" stop-color="var(--gold-dark)"/>
        <stop offset="0.5" stop-color="var(--gold)"/>
        <stop offset="1" stop-color="var(--gold-light)"/>
      </linearGradient>
    </defs>
    <path class="hero-photo" role="img" aria-label="Group of smiling authors on stage holding up their newly launched books in front of an event backdrop"
          d="M0 0 H1200 V400 C1000 640 400 700 0 298 Z" fill="url(#photoTone)"/>
    <path class="swoosh swoosh--main" d="M0 298 C400 700 1000 640 1200 400 L1200 432 C1000 690 520 770 0 612 Z" fill="url(#goldTone)"/>
    <path class="swoosh-line" d="M0 500 C300 640 620 680 870 650" fill="none" stroke="var(--navy)" stroke-width="4"/>
    <path class="swoosh swoosh--corner" d="M714 1150 C850 1020 1100 985 1200 1060 L1200 1200 C1130 1095 950 1045 714 1150 Z" fill="url(#goldTone)"/>
  </svg>

  <div class="brand"><span class="brand__mark"></span><span class="brand__name">Bravolin Hub</span></div>

  <p class="eyebrow">Webinar</p>
  <h1 class="headline">Steps to Unveil your venture<br>with poise and polish</h1>
  <p class="intro">Join us for this webinar to learn all about 'Steps to Unveil your venture with poise and polish'. You'll know exactly what steps to take in order to make sure your book is launched with the exposure it deserves. We'll also cover how to effectively promote yourself, increase visibility, get press coverage.</p>

  <div class="schedule">
    <p class="schedule__label">Time &amp; Date</p>
    <p class="schedule__time">15 Mar, 7:00 pm – 8:00 pm AEDT</p>
  </div>

  <p class="site">www.bravolinhub.com.au</p>
</main>
</body>
</html>
```